Guaranteed Job - Sleek Sexy Business Card UV Spot

Im looking for a sleek and sexy business card, that resembles elite or VIP status status.
our business is corinvale.example
you can view our products on there, but our main audience for handing out our cards will be for people in the hospitality industry, so it will need to impress high management and CEO of hotels and restaurants, bars, clubs etc...
the card features will have UV spot on both sides, 400gsm stock. standard size.
Artwork should be 86 x 54mm + 2mm bleed = 90 x 58mm
it should have a nice "unique" uv spot pattern that highlights the card, not a repeated pattern, theres no originality there, and it will be disregarded.
The written material will be:
Corin Vale Hospitality College (logo)
Tobin Marsh
Director
Phone: 1300 615 737
Mobile: 0455 817 296
Email: info@corinvale.example
website: www.corinvale.example
I'm looking for originality here, i don't want just a simple stock card, want something that has a wow factor for people.
You will find the logo attached. you may invert the white to black words to suit the background as you please.
thank you and good luck
As a side note, ive received a lot of proposals, im too busy to give feedback to each and every one, so if i havent provided feedback for your design within 24 hours, then consider it not acceptable, and you could resubmit another design.
So far i have not seen any design that stood out for me, they all seem pretty generic. there nothing thats unique, i would figure for the amount that im offering, that people would put some more effort and creativity into the design.
so far over 200 designs submitted, and nothing i have seen looks very original, everything looks like a different variation of the same stuff, i said it very clearly i wanted something unique, the only thing that has come close to it so far is this one
Reason: Ive received alot of design concepts and i have reviewed everyone, but i havent had time to give feedback to every single one, only the ones that have interested me, if i havent responded, its because i havent found it good enough.
so far only a few design have been on par with what ive been looking for, an attractive eye popping design.
heres a few of them,
http://files.pixelbazaar.example/design_img/51736/62418/62418_2840915_51736_image.jpg
http://files.pixelbazaar.example/design_img/51736/68254/68254_2841377_51736_image.jpg
theyre, both unique and original, and eye catching, the only thing theyre missing is the sexyness.
if you still think you have some creativity left in your minds, then throw it on here.
Reason: Sorry guys for the delay, I was in a serious accident and out of commission for the past few months, I'm just slowly recovering now, please bare with me as i try to attend to this project, it may take me awhile as I have other projects that are on standby, I'm not 100% at the moment, so im extending the deadline for 2 weeks right now. Thanks for your patience.
Hospitality

```html
<!DOCTYPE html>
<html lang="en">
<head>
<meta charset="utf-8">
<title>Corin Vale Hospitality College – Business Card</title>
<link rel="stylesheet" href="https://fonts.googleapis.com/css2?family=Montserrat:wght@500;700&family=Arimo:wght@400&display=swap">
<style>
  :root {
    --bg: #e8e3da;
    --card-black: #0b0b0b;
    --texture-light: #1c1c1c;
    --teal: #1ab39f;
    --white: #ffffff;
    --sky: #4a9fe0;
    --ink: #111111;
  }
  * { margin: 0; padding: 0; box-sizing: border-box; }
  html, body { width: 1200px; height: 900px; overflow: hidden; background: var(--bg); }
  .canvas {
    width: 1200px; height: 900px;
    display: flex; flex-direction: column; align-items: center; justify-content: center;
    gap: 40px;
  }
  .card {
    position: relative;
    width: 620px; height: 390px;
    overflow: hidden;
    box-shadow: 0 10px 24px rgba(0,0,0,0.25);
    background: var(--card-black);
  }
  .card svg.art { position: absolute; inset: 0; }
  .texture {
    position: absolute; inset: 0;
    background: radial-gradient(ellipse at 40% 60%, var(--texture-light), var(--card-black) 75%);
  }
  .wordmark {
    position: absolute;
    font-family: "Montserrat", sans-serif;
    font-weight: 700;
    text-transform: uppercase;
    line-height: 1.05;
    display: flex; align-items: center; gap: 14px;
  }
  .wordmark .mark-square { width: 34px; height: 34px; background: currentColor; flex: none; }
  .wordmark .name-main { display: block; font-size: 30px; letter-spacing: 1px; }
  .wordmark .name-sub { display: block; font-size: 13px; letter-spacing: 1.5px; }

  .front .wordmark { right: 34px; top: 40px; color: var(--ink); }

  .person { position: absolute; left: 40px; top: 186px; }
  .person-name {
    font-family: "Montserrat", sans-serif; font-weight: 700;
    font-size: 28px; color: var(--sky);
  }
  .person-role {
    font-family: "Arimo", sans-serif; font-size: 19px; color: var(--white); margin-top: 2px;
  }
  .contact {
    position: absolute; left: 40px; top: 286px;
    font-family: "Arimo", sans-serif; font-size: 15px; line-height: 1.65; color: var(--white);
  }

  .back .wordmark {
    left: 50%; top: 50%; transform: translate(-50%, -50%);
    color: var(--white);
  }
  .back .wordmark .name-main { font-size: 40px; }
  .back .wordmark .name-sub { font-size: 17px; }
  .back .wordmark .mark-square { width: 46px; height: 46px; }
</style>
</head>
<body>
<main class="canvas">

  <section class="card front">
    <div class="texture" role="img" aria-label="Dark crumpled paper texture in black and charcoal"></div>
    <svg class="art" width="620" height="390" viewBox="0 0 620 390" aria-hidden="true">
      <defs>
        <pattern id="teal-stripes" width="40" height="40" patternUnits="userSpaceOnUse" patternTransform="rotate(-12)">
          <rect width="40" height="40" fill="var(--teal)"/>
          <rect y="0" width="40" height="15" fill="var(--white)"/>
        </pattern>
      </defs>
      <rect class="stripe-band" x="0" y="0" width="620" height="152" fill="url(#teal-stripes)"/>
      <polygon class="logo-panel" points="200,152 340,0 620,0 620,152" fill="var(--white)"/>
      <rect class="accent-rule" x="0" y="152" width="620" height="6" fill="var(--teal)"/>
    </svg>

    <div class="wordmark">
      <span class="mark-square"></span>
      <span>
        <span class="name-main">Corin Vale</span>
        <span class="name-sub">Hospitality College</span>
      </span>
    </div>

    <div class="person">
      <p class="person-name">Tobin Marsh</p>
      <p class="person-role">Director</p>
    </div>

    <div class="contact">
      <p>Phone: 1300 615 737, Mobile: 0455 817 296</p>
      <p>Email: info@corinvale.example, website: www.corinvale.example</p>
    </div>
  </section>

  <section class="card back">
    <div class="texture" role="img" aria-label="Dark crumpled paper texture in black and charcoal"></div>
    <svg class="art" width="620" height="390" viewBox="0 0 620 390" aria-hidden="true">
      <defs>
        <pattern id="white-stripes" width="12" height="12" patternUnits="userSpaceOnUse" patternTransform="rotate(35)">
          <rect width="12" height="12" fill="none"/>
          <rect width="6" height="12" fill="var(--white)"/>
        </pattern>
      </defs>
      <polygon class="corner-stripes top" points="0,0 150,0 130,22 0,22" fill="url(#white-stripes)"/>
      <polygon class="corner-stripes bottom" points="490,368 620,368 620,390 470,390" fill="url(#white-stripes)"/>
    </svg>

    <div class="wordmark">
      <span class="mark-square"></span>
      <span>
        <span class="name-main">Corin Vale</span>
        <span class="name-sub">Hospitality College</span>
      </span>
    </div>
  </section>

</main>
</body>
</html>
```